Summer Sale Graphics for Social Media

I want to create 11 social media graphics (new Instagram size 4:5 (1080 x 1350 pixels) focusing on our Summer Sale Graphics, using any of the pics attached. Use the attached pics, NO RANDOM STOCK PHOTOGRAPHY. For the color scheme of the graphics, they should all be complementary to the product colors in the photos.
You can add any of the photos attached but none are required. You can do some of the graphics in all text. I mainly need BOLD text that says one of the headlines (11 total) SEE ATTACHED WORD DOCUMENT for the headlines to use.

```html
<!DOCTYPE html>
<html lang="en">
<head>
<meta charset="utf-8">
<title>Summer Sale Social Set</title>
<link rel="stylesheet" href="https://fonts.googleapis.com/css2?family=Bebas+Neue&display=swap">
<style>
  :root{
    --board:#2b2b2b;
    --plum:#7d4a84;
    --plum-deep:#6b3b72;
    --cream:#eeebe9;
    --white:#ffffff;
    --skin-glow:#e6dde2;
    --rose-mist:#c9afbd;
    --warm:#7f5a55;
    --brown-top:#8b6a5c;
  }
  *{box-sizing:border-box;margin:0;padding:0}
  html,body{width:1200px;height:904px;overflow:hidden;background:var(--board)}
  body{position:relative;font-family:"Bebas Neue",sans-serif;color:var(--white)}

  .tile{position:absolute;overflow:hidden;background:var(--plum)}
  .tile--hero{left:35px;top:30px;width:443px;height:555px}
  .tile--sm{width:216px;height:269px}

  /* Photo stand-in: soft light glow where the person stands, fading into plum on the text side */
  .photo{position:absolute;inset:0;
    background:
      linear-gradient(90deg,var(--plum) 0%,var(--plum) 34%,rgba(125,74,132,.55) 52%,rgba(125,74,132,0) 72%),
      radial-gradient(ellipse 38% 34% at 74% 52%,var(--skin-glow) 0%,rgba(230,221,226,.6) 45%,rgba(230,221,226,0) 100%),
      radial-gradient(ellipse 60% 70% at 76% 60%,var(--rose-mist) 0%,rgba(201,175,189,0) 75%),
      linear-gradient(180deg,#8a5f66 0%,#7f5576 55%,#7d4a84 100%);}
  .photo--brown{
    background:
      linear-gradient(90deg,var(--plum) 0%,var(--plum) 36%,rgba(125,74,132,.5) 55%,rgba(125,74,132,0) 74%),
      radial-gradient(ellipse 30% 42% at 76% 58%,var(--brown-top) 0%,rgba(139,106,92,.5) 55%,rgba(139,106,92,0) 100%),
      radial-gradient(ellipse 60% 60% at 80% 90%,#9b3e5e 0%,rgba(155,62,94,0) 70%),
      linear-gradient(180deg,#8d6a5a 0%,#7e5470 60%,#7d4a84 100%);}
  .photo--hero{
    background:
      linear-gradient(90deg,var(--plum) 0%,var(--plum) 26%,rgba(125,74,132,.5) 42%,rgba(125,74,132,0) 60%),
      radial-gradient(ellipse 34% 30% at 68% 46%,var(--skin-glow) 0%,rgba(230,221,226,.55) 50%,rgba(230,221,226,0) 100%),
      linear-gradient(180deg,rgba(0,0,0,0) 80%,rgba(238,235,233,.55) 90%,rgba(125,74,132,.9) 100%),
      radial-gradient(ellipse 70% 60% at 72% 55%,var(--rose-mist) 0%,rgba(201,175,189,0) 75%),
      linear-gradient(180deg,#8b5a5a 0%,#7e5070 60%,#7d4a84 100%);}

  /* Product shot stand-in: light studio backdrop with soft label tones */
  .scene{position:absolute;inset:0;
    background:radial-gradient(ellipse at 50% 65%,#f8f6f5 0%,var(--cream) 60%,#dcd8d6 100%)}
  .products{position:absolute;left:8%;right:8%;border-radius:10px;filter:blur(3px);
    background:
      radial-gradient(ellipse 14% 30% at 14% 62%,#d98bb3 0%,rgba(217,139,179,0) 100%),
      radial-gradient(ellipse 14% 30% at 38% 62%,#d8474f 0%,rgba(216,71,79,0) 100%),
      radial-gradient(ellipse 14% 30% at 62% 62%,#3f8f78 0%,rgba(63,143,120,0) 100%),
      radial-gradient(ellipse 14% 30% at 86% 62%,#3e56a4 0%,rgba(62,86,164,0) 100%),
      linear-gradient(180deg,#fbfbfb 0%,#f1eff0 70%,#d8d3d3 100%);}

  .curve{position:absolute;left:0;top:0;width:100%}
  .copy{position:absolute;line-height:.9;text-transform:uppercase}
  .copy--center{left:0;right:0;text-align:center}
  .badge{position:absolute;background:var(--white);color:var(--plum);font-size:12.5px;line-height:1;padding:3px 7px 2px;letter-spacing:.2px;white-space:nowrap}
  .badge--center{left:50%;transform:translateX(-50%)}
  .badge--plum{background:var(--plum);color:var(--white)}
  .badge--dark{background:var(--plum-deep);color:var(--white);text-align:center;padding:4px 6px}
  .boxed{position:absolute;border:1.5px solid var(--white);line-height:.82}
  .rule{position:absolute;height:1.5px;background:var(--white)}
  .bar{position:absolute;background:var(--plum)}
</style>
</head>
<body>

<!-- Hero -->
<section class="tile tile--hero">
  <div class="photo photo--hero" role="img" aria-label="Smiling woman in a white crop sweater holding a supplement bottle in a kitchen, bottles on the counter"></div>
  <div class="copy" style="left:26px;top:28px;font-size:56px;line-height:.92">Your<br>Summer<br>Body Won’t<br>Wait</div>
  <div class="boxed" style="left:28px;top:246px;width:163px;height:195px;padding:8px 0 0 10px;font-size:100px">Sale<br>Now!</div>
  <div class="badge" style="left:27px;top:487px;font-size:19px;padding:5px 9px 3px">Up to $15 off</div>
</section>

<!-- Row 1 -->
<section class="tile tile--sm" style="left:491px;top:30px">
  <div class="photo" role="img" aria-label="Woman in white crop sweater smiling beside a row of supplement bottles"></div>
  <div class="copy" style="left:9px;top:22px;font-size:21px">Get snatched<br>for summer</div>
  <div class="copy" style="left:9px;top:71px;font-size:19px">Supplements on</div>
  <div class="copy" style="left:8px;top:93px;font-size:70px;line-height:.82">Sale<br>Now!</div>
  <div class="badge" style="left:8px;top:236px">Up to $15 off</div>
</section>

<section class="tile tile--sm" style="left:719px;top:30px">
  <div class="scene"></div>
  <div class="products" style="top:140px;height:95px" role="img" aria-label="Four white supplement bottles with pink, red, green and blue labels"></div>
  <svg class="curve" viewBox="0 0 216 130" height="130" aria-hidden="true"><path d="M0 0H216V100Q108 160 0 100Z" fill="var(--plum)"/></svg>
  <div class="copy copy--center" style="top:16px;font-size:22px">One sale. One body.</div>
  <div class="copy copy--center" style="top:38px;font-size:37px;line-height:.95">One summer<br>to slay</div>
  <div class="badge badge--plum badge--center" style="top:244px">Up to $15 off</div>
</section>

<section class="tile tile--sm" style="left:949px;top:30px">
  <div class="photo" role="img" aria-label="Woman in white crop sweater pointing to supplement bottles on a counter"></div>
  <div class="copy" style="left:11px;top:18px;font-size:50px;line-height:.85">Hurry!</div>
  <div class="copy" style="left:11px;top:66px;font-size:21px">Our summer<br>slim down<br>sale is on<br>don’t<br>miss it!</div>
  <div class="badge" style="left:15px;top:244px">Up to $15 off</div>
</section>

<!-- Row 2 -->
<section class="tile tile--sm" style="left:491px;top:316px">
  <div class="scene"></div>
  <div class="products" style="top:135px;height:100px" role="img" aria-label="Four supplement bottles lined up on a light surface"></div>
  <svg class="curve" viewBox="0 0 216 140" height="140" aria-hidden="true"><path d="M0 0H216V105Q108 150 0 105Z" fill="var(--plum)"/></svg>
  <div class="copy copy--center" style="top:12px;font-size:20px">Slim waist. Flat<br>tummy. More<br>energy. Let’s go!</div>
  <div class="copy copy--center" style="top:68px;font-size:47px">Sale Now!</div>
  <div class="badge badge--plum badge--center" style="top:245px">Up to $15 off</div>
</section>

<section class="tile tile--sm" style="left:719px;top:316px">
  <div class="photo" role="img" aria-label="Woman in white crop sweater holding a supplement bottle in a kitchen"></div>
  <div class="copy" style="left:12px;top:13px;font-size:24px">Summer<br>isn’t waiting<br>neither<br>should you</div>
  <div class="boxed" style="left:12px;top:116px;width:80px;height:95px;padding:6px 0 0 4px;font-size:50px">Sale<br>Now!</div>
  <div class="badge" style="left:12px;top:236px">Up to $15 off</div>
</section>

<section class="tile tile--sm" style="left:949px;top:316px">
  <div class="scene"></div>
  <div class="products" style="top:138px;height:100px" role="img" aria-label="Four supplement bottles lined up on a light surface"></div>
  <svg class="curve" viewBox="0 0 216 140" height="140" aria-hidden="true"><path d="M0 0H216V105Q108 150 0 105Z" fill="var(--plum)"/></svg>
  <div class="copy copy--center" style="top:12px;font-size:20px">Final countdown to</div>
  <div class="copy copy--center" style="top:33px;font-size:45px;line-height:.88">Summer<br>sale now!</div>
  <div class="bar" style="left:76px;top:247px;width:65px;height:12px"></div>
</section>

<!-- Row 3 -->
<section class="tile tile--sm" style="left:261px;top:601px;width:217px">
  <div class="photo" role="img" aria-label="Woman in white crop sweater smiling behind a row of supplement bottles"></div>
  <div class="copy" style="left:10px;top:22px;font-size:20px">Detox,<br>burn fat, and<br>turn heads<br>this summer</div>
  <div class="copy" style="left:9px;top:96px;font-size:62px;line-height:.84">Sale<br>Now!</div>
  <div class="badge badge--dark" style="left:11px;top:240px">Up to<br>$15 off</div>
</section>

<section class="tile tile--sm" style="left:491px;top:601px">
  <div class="photo photo--brown" role="img" aria-label="Woman in brown top and black jeans holding supplement bottles in a games room"></div>
  <div class="copy" style="left:9px;top:12px;font-size:84px;line-height:.85">Sale</div>
  <div class="copy" style="left:9px;top:86px;font-size:28px;line-height:.95">Your<br>summer<br>body<br>starts<br>here</div>
  <div class="badge" style="left:12px;top:241px">Up to $15 off</div>
</section>

<section class="tile tile--sm" style="left:719px;top:601px">
  <div class="photo" role="img" aria-label="Woman in white crop sweater holding a supplement bottle"></div>
  <div class="copy" style="left:11px;top:18px;font-size:23px">Limited-time</div>
  <div class="copy" style="left:11px;top:42px;font-size:56px;line-height:.85">Summer<br>sale</div>
  <div class="rule" style="left:11px;top:139px;width:88px"></div>
  <div class="copy" style="left:11px;top:149px;font-size:22px">Snatch your<br>supplements<br>now!</div>
  <div class="badge" style="left:11px;top:241px">Up to $15 off</div>
</section>

<section class="tile tile--sm" style="left:949px;top:601px">
  <div class="photo photo--brown" role="img" aria-label="Woman in brown top holding supplement bottles in a games room"></div>
  <div class="copy" style="left:10px;top:20px;font-size:24px">Summer’s here.<br>And we’re<br>having the</div>
  <div class="copy" style="left:10px;top:117px;font-size:46px;line-height:.85">Biggest<br>sale</div>
  <div class="copy" style="left:10px;top:197px;font-size:24px">Of the year</div>
  <div class="badge" style="left:14px;top:245px">Up to $15 off</div>
</section>

</body>
</html>
```